Billboard design for agricultural machinery business

hello im looking for roadside advertiement sign to be designed, the sign is 10ft up in the air and is 4ft high and 8ft wide, id image i like a blue background and my logo front and centre and below logo sales - service - parts and then below that the brook meadow symbol and vale symbol, I’d also like the website www.Fernowell.ie on it. i am open to suggestions and designs. blue is #005999 and yellow is rgb (254, 205, 26) ive attached my log and symbols, im open to different colour backgrounds or just white and also open to brook meadow and vale as writhing rather than logos

Target Market(s)

Brook Meadow and vale tractor owners

Industry/Entity Type

Agricultural machine sales service and parts

Colors

Designer to choose colors to be used in the design.

Requirements
Must have
• My logo and colours, brands brook Meadow and vale, website

```html
<!DOCTYPE html>
<html lang="en">
<head>
<meta charset="utf-8">
<title>Fernowell Roadside Billboard</title>
<link href="https://fonts.googleapis.com/css2?family=Montserrat:ital,wght@0,700;0,800;1,700;1,800&display=swap" rel="stylesheet">
<style>
  :root {
    --brand-blue: #005999;
    --deep-blue: #0b4a86;
    --brand-yellow: rgb(254, 205, 26);
    --navy-ink: #0d2f57;
    --sky-top: #9fd3ee;
    --sky-low: #eef4e6;
    --field-green: #4f9a2c;
    --field-dark: #2f6e1c;
    --white: #ffffff;
    --page: #ffffff;
  }
  html, body {
    margin: 0;
    padding: 0;
    width: 1200px;
    height: 1200px;
    overflow: hidden;
    background: var(--page);
  }
  .canvas {
    position: relative;
    width: 1200px;
    height: 1200px;
  }
  .billboard {
    position: absolute;
    left: 124px;
    top: 362px;
    width: 952px;
    height: 476px;
    display: block;
  }
  .brand-name {
    font-family: "Montserrat", sans-serif;
    font-weight: 800;
    fill: var(--white);
  }
  .service-line {
    font-family: "Montserrat", sans-serif;
    font-weight: 800;
    font-style: italic;
    fill: var(--navy-ink);
  }
  .web-address {
    font-family: "Montserrat", sans-serif;
    font-weight: 700;
    font-style: italic;
    fill: var(--white);
    letter-spacing: 4px;
  }
  .partner-name {
    font-family: "Montserrat", sans-serif;
    font-weight: 800;
    fill: var(--navy-ink);
  }
</style>
</head>
<body>
<div class="canvas">
  <svg class="billboard" viewBox="0 0 952 476" xmlns="http://www.w3.org/2000/svg">
    <defs>
      <linearGradient id="field-scene" x1="0" y1="0" x2="0" y2="1">
        <stop offset="0" stop-color="var(--sky-top)"/>
        <stop offset="0.42" stop-color="var(--sky-low)"/>
        <stop offset="0.5" stop-color="#8fb86a"/>
        <stop offset="0.62" stop-color="var(--field-green)"/>
        <stop offset="1" stop-color="var(--field-dark)"/>
      </linearGradient>
    </defs>

    <rect class="panel-base" x="0" y="0" width="952" height="476" fill="var(--white)"/>

    <rect class="field-photo" x="0" y="0" width="952" height="354" fill="url(#field-scene)"
          role="img" aria-label="Photograph of green crop rows in a farm field under a bright summer sky"/>

    <polygon class="centre-panel" points="308,0 644,0 817,354 134,354" fill="var(--brand-blue)"/>

    <rect class="base-strip" x="0" y="354" width="952" height="11" fill="var(--deep-blue)"/>
    <path class="web-tab" d="M212 365 H744 V427 Q744 443 728 443 H228 Q212 443 212 427 Z" fill="var(--deep-blue)"/>

    <text class="brand-name" x="447" y="208" text-anchor="middle" font-size="74">Fernowell</text>

    <polygon class="service-band" points="167,286 784,286 814,347 137,347" fill="var(--brand-yellow)"/>
    <text class="service-line" x="476" y="331" text-anchor="middle" font-size="38">SALES • SERVICE • PARTS</text>

    <text class="web-address" x="478" y="416" text-anchor="middle" font-size="33">WWW.FERNOWELL.IE</text>

    <text class="partner-name" x="112" y="418" text-anchor="middle" font-size="21">BROOK MEADOW</text>
    <text class="partner-name" x="840" y="420" text-anchor="middle" font-size="30">VALE</text>
  </svg>
</div>
</body>
</html>
```